letterhead design using our existing logo

We are a small boutique property management business based in Sydney's Northern Beaches.
We are after a sleek, simple modern letterhead (A4) incorporating our logo and its colours.
Also matching envelope (DL)
I have attached the logo with black text and white text for design options.

Target Market(s)

29-69yo Male and Female

Industry/Entity Type

Property Management

Requirements
Must have
• - Estate Haven logo
• - Address, number and website:
• Suite 7, 18-19 Harlow Parade, Brenton NSW 2187
• Tel: Carl Doyle 0419 267 530 Miriam Kovacs 0407 516 948 www.estatehavenrealty.com.au
Nice to have
• sleek design that looks modern and professional
Should not have
• too many colours or too busy

```html
<!DOCTYPE html>
<html lang="en">
<head>
<meta charset="utf-8">
<title>Estate Haven – Letterhead &amp; DL Envelope</title>
<link rel="stylesheet" href="https://fonts.googleapis.com/css2?family=Open+Sans:ital,wght@0,400;0,600;0,700;0,800;1,400;1,600&display=swap">
<style>
  :root {
    --teal: #23919b;
    --teal-deep: #1d7f88;
    --teal-ghost: rgba(255,255,255,0.07);
    --ink: #1c1c1c;
    --grey: #555a60;
    --paper: #ffffff;
    --backdrop: #e6e8eb;
    --rule: #c9cdd1;
  }
  * { box-sizing: border-box; margin: 0; padding: 0; }
  html, body { width: 1200px; height: 1200px; overflow: hidden; }
  body {
    background: var(--backdrop);
    font-family: "Open Sans", Arial, sans-serif;
    position: relative;
  }

  /* ---------- A4 letterhead ---------- */
  .letterhead {
    position: absolute;
    left: 60px; top: 204px;
    width: 560px; height: 792px;
    background: var(--paper);
    box-shadow: 0 6px 20px rgba(0,0,0,0.12);
    overflow: hidden;
  }
  .letterhead__band {
    position: absolute; left: 0; top: 0; bottom: 0;
    width: 92px;
    background: linear-gradient(180deg, var(--teal) 0%, var(--teal-deep) 100%);
    border-right: 3px solid var(--paper);
    box-shadow: 1px 0 0 var(--teal);
    overflow: hidden;
  }
  .band-word {
    position: absolute;
    left: 50%; top: 50%;
    transform: translate(-50%, -50%) rotate(-90deg);
    white-space: nowrap;
    font-weight: 800;
    font-size: 96px;
    letter-spacing: 4px;
    color: var(--teal-ghost);
  }
  .letterhead__brand {
    position: absolute;
    right: 44px; top: 44px;
  }
  .brand-name {
    display: flex; align-items: center; gap: 8px;
    font-weight: 800;
    font-size: 22px;
    letter-spacing: 0.5px;
    text-transform: uppercase;
    color: var(--ink);
  }
  .brand-dot {
    width: 12px; height: 12px; border-radius: 50%;
    background: var(--teal);
  }
  .letterhead__footer {
    position: absolute;
    left: 118px; bottom: 36px; right: 30px;
    display: flex; align-items: flex-start; gap: 14px;
    font-size: 9.5px;
    color: var(--grey);
  }
  .contacts { display: grid; grid-template-columns: auto auto; column-gap: 10px; row-gap: 3px; align-items: baseline; }
  .contact-name { color: var(--teal); font-weight: 600; font-size: 11px; }
  .footer-divider { width: 1px; align-self: stretch; background: var(--rule); }
  .footer-details { display: flex; flex-direction: column; gap: 4px; padding-top: 1px; }

  /* ---------- DL envelope ---------- */
  .envelope {
    position: absolute;
    left: 660px; top: 480px;
    width: 500px; height: 250px;
    background: var(--paper);
    box-shadow: 0 6px 20px rgba(0,0,0,0.12);
    overflow: hidden;
  }
  .envelope__brand { position: absolute; left: 30px; top: 26px; }
  .envelope__brand .brand-name { font-size: 17px; }
  .envelope__address {
    margin-top: 6px;
    font-size: 8.5px;
    line-height: 1.45;
    color: var(--grey);
  }
  .envelope__band {
    position: absolute; left: 0; right: 0; bottom: 0;
    height: 66px;
    background: linear-gradient(90deg, var(--teal-deep) 0%, var(--teal) 100%);
    border-top: 3px solid var(--paper);
    box-shadow: 0 -1px 0 var(--teal);
    overflow: hidden;
  }
  .envelope__band .band-word {
    transform: translate(-50%, -50%);
    font-size: 72px;
  }
</style>
</head>
<body>

  <section class="letterhead" aria-label="A4 letterhead">
    <div class="letterhead__band"><span class="band-word">ESTATE HAVEN</span></div>

    <header class="letterhead__brand">
      <div class="brand-name"><span class="brand-dot"></span>Estate Haven</div>
    </header>

    <footer class="letterhead__footer">
      <div class="contacts">
        <span class="contact-name">Carl Doyle</span><span>0419 267 530</span>
        <span class="contact-name">Miriam Kovacs</span><span>0407 516 948</span>
      </div>
      <span class="footer-divider"></span>
      <div class="footer-details">
        <span>www.estatehavenrealty.com.au</span>
        <span>Suite 7, 18-19 Harlow Parade, Brenton NSW 2187</span>
      </div>
    </footer>
  </section>

  <section class="envelope" aria-label="DL envelope">
    <div class="envelope__brand">
      <div class="brand-name"><span class="brand-dot"></span>Estate Haven</div>
      <p class="envelope__address">Suite 7, 18-19 Harlow Parade<br>Brenton NSW 2187</p>
    </div>
    <div class="envelope__band"><span class="band-word">ESTATE HAVEN</span></div>
  </section>

</body>
</html>
```